Cobalt Ridge Mini Storage - Ad for half Page

Need half page ad for a publication.
would also like to be able to use in the future
self storage facility - 3 locations, the third opening soon
do not like real busy projects...i have a logo but willing to tweak if needed

```html
<!DOCTYPE html>
<html lang="en">
<head>
<meta charset="utf-8">
<title>Cobalt Ridge Mini Storage – Opening Soon</title>
<link rel="stylesheet" href="https://fonts.googleapis.com/css2?family=Montserrat:wght@700;800&display=swap">
<style>
  :root {
    --page: #444442;
    --sun-top: #fdc700;
    --sun-bottom: #eaa700;
    --ribbon-light: #9c5d10;
    --ribbon-dark: #6b3404;
    --panel-light: #302e2f;
    --panel-dark: #110303;
    --headline-white: #eef6fb;
    --headline-gold: #f7bb00;
    --headline-gold-deep: #f0aa00;
    --brand-brown: #5c2e0c;
    --brand-mark: #a0620f;
  }
  html, body {
    margin: 0;
    padding: 0;
    width: 1200px;
    height: 1200px;
    overflow: hidden;
    background: var(--page);
  }
  .canvas {
    width: 1200px;
    height: 1200px;
    display: flex;
    align-items: center;
    justify-content: center;
  }
  .ad {
    display: block;
    width: 1200px;
    height: 797px;
  }
  .brand-name {
    font-family: "Montserrat", sans-serif;
    font-weight: 800;
    font-size: 36px;
    fill: var(--brand-brown);
  }
  .headline {
    font-family: "Montserrat", sans-serif;
    font-weight: 800;
  }
  .headline--opening { fill: var(--headline-white); font-size: 180px; }
  .headline--soon { fill: url(#goldType); font-size: 265px; }
</style>
</head>
<body>
<main class="canvas">
  <svg class="ad" viewBox="0 0 1495 993" xmlns="http://www.w3.org/2000/svg" aria-labelledby="adTitle">
    <title id="adTitle">Cobalt Ridge Mini Storage – Opening Soon</title>
    <defs>
      <linearGradient id="sunField" x1="0" y1="0" x2="0" y2="1">
        <stop offset="0" stop-color="var(--sun-top)"/>
        <stop offset="1" stop-color="var(--sun-bottom)"/>
      </linearGradient>
      <linearGradient id="ribbonShade" x1="0" y1="0" x2="1" y2="0.3">
        <stop offset="0" stop-color="var(--ribbon-light)"/>
        <stop offset="0.55" stop-color="#8a4c0b"/>
        <stop offset="1" stop-color="var(--ribbon-dark)"/>
      </linearGradient>
      <linearGradient id="goldType" x1="0" y1="0" x2="0" y2="1">
        <stop offset="0" stop-color="var(--headline-gold)"/>
        <stop offset="1" stop-color="var(--headline-gold-deep)"/>
      </linearGradient>
    </defs>

    <!-- background -->
    <rect class="ad-field" x="0" y="0" width="1495" height="993" fill="url(#sunField)"/>

    <!-- brand -->
    <g class="brand">
      <rect class="brand-mark" x="52" y="55" width="80" height="80" fill="var(--brand-mark)"/>
      <text class="brand-name" x="152" y="88">Cobalt Ridge</text>
      <text class="brand-name" x="152" y="130">Mini Storage</text>
    </g>

    <!-- lower panel -->
    <g class="panel-soon">
      <polygon points="276,643 1192,481 1190,787 264,956" fill="var(--panel-dark)"/>
      <polygon points="276,643 1192,481 264,956" fill="var(--panel-light)"/>
    </g>

    <!-- upper ribbon -->
    <g class="ribbon-opening">
      <polygon points="221,375 1254,189 1246,471 207,657" fill="url(#ribbonShade)"/>
      <polygon points="600,390 1246,471 207,657" fill="#5a2a02" opacity="0.18"/>
    </g>

    <!-- headline -->
    <text class="headline headline--opening" transform="translate(712,488) rotate(-10) skewX(-6)"
          text-anchor="middle" textLength="840" lengthAdjust="spacingAndGlyphs">OPENING</text>
    <text class="headline headline--soon" transform="translate(728,808) rotate(-9.5) skewX(-6)"
          text-anchor="middle" textLength="650" lengthAdjust="spacingAndGlyphs">SOON</text>
  </svg>
</main>
</body>
</html>
```